International Health Supplement Company Needs Packaging and Label Redesign

Copper Lantern LLC requires a redesign for 1 internationally sold product and accompanying designs for 5 additional products. The additional products are currently sold locally and yet to be released internationally.

Our company is honest, premium, and passionate about supplements. We adopt a 'no BS' stance and as such source only the finest ingredients and deliver high-quality liquid health supplements to customers globally. We do not compromise on quality and do not apologise for price.

We want a clean, crisp design that conveys ‘premium, cutting-edge, boutique’ at a glance. We feel our current design appeals more to the 'chest beaters' rather than the 'chess players' that our research has indicated are our customers.

We have SIX PRODUCTS TOTAL in our range and feel individual color cues to distinguish the different products would greatly assist customer navigation i.e. Customers will identify ‘red’ means ‘product X’ without reading the label. (Examples attached and below we believe do this well).

Current 30ml bottle, cap, and dropper are in black and will remain so. Current label is black, however, we have a white label on our local product (example attached) and prefer the look of it.

Packaging is currently black and could remain so however most products that appeal to our target market are in white with color accents.

One consideration we have is that the product up until now has been selling exceptionally well so we need to retain some kind of familiarity with the existing branding. Perhaps that’s just the logo.

Logo can be revised i.e. add company name and/or company slogan.

Products are: (Function - Name)

Testosterone Support - Tongkat Ali (current)
Hormone Support - Jiaogulan
Energy Support - Ashwaghanda
Libido Support - Krachai Dam (for men)
Libido Support - Kacip Fatimah (for women)
Sleep Support - Wild Chamomile

Packaging: 4.6cm (L) x 8.0cm (W) x 11.2cm (H)
Label: 30 mL bottle

https://www.folioweb.example/gallery/TONIC-BOX-STUDY-2011/7402518
http://www.pelkastudio.example/projects/#/river-tea/
https://www.folioweb.example/gallery/31420786/Velmora-Skin
https://au.pinboardly.example/pin/592719083317915736/
https://au.pinboardly.example/pin/36916877689752218/
http://velto.example/en/portfolio/logo-redesign/

Target Market(s)

Generation X Men (and their partners), 36-55, upper middle class, who appreciate quality products.

Industry/Entity Type

Health Product

Font styles to use
Serif
Sans Serif

Requirements
Must have
• Packaging - Principal Display Panel (Front):
• 1. Function & Name of each product i.e 'Testosterone Support' & 'Tongkat Ali'
• 2. '30ml' AND '1 fl oz' (text size 1.8in / 3.2mm / 9 point min.)
• 3. 'Dietary Supplement'
• Packaging - Information Panel (Right):
• 1. Supplement Facts Panel (template accepted for drafts)
• 2. Directions: (lorum ipsum accepted for drafts)
• 3. Safety Warning: (lorum ipsum accepted for drafts)
• 4. 'Manufactured for: Copper Lantern LLC'
• 5. 'Sheridan, Wyoming'
• 6. '(414) 563 2180'
• 7. 'Product of Thailand'
• Bottle Label:
• 3. 'Dietary Supplement'
• 4. Supplement Facts Panel (template accepted for drafts)
• 5. Directions: (lorum ipsum accepted for drafts)
• 6. Safety Warning: (forum ipsum accepted for drafts)
• 7. 'Manufactured for: Copper Lantern LLC'
• 8. 'Sheridan, Wyoming'
• 9. '(414) 563 2180'
• 10. 'Product of Thailand'
Nice to have
• Updated logo with company name 'Copper Lantern' and/or company slogan 'Quality Without Compromise' added.
Should not have
• No photos or stock images.
• No elements of the current design (excluding logo) to remain i.e. 'Otter Finn', 'Testosterone Booster', 'Increase Lean Muscle', 'Stabilise Hormones', 'Boost Endurance', 'Improve Muscle Naturally', are all to be omitted.

```html
<!DOCTYPE html>
<html lang="en">
<head>
<meta charset="utf-8">
<title>Copper Lantern — Testosterone Support Packaging</title>
<link rel="stylesheet" href="https://fonts.googleapis.com/css2?family=Roboto+Condensed:wght@300;400;700&family=Exo+2:ital,wght@1,300&family=Josefin+Sans:wght@400&display=swap">
<style>
  :root {
    --gold: #c9a82c;
    --gold-bright: #e2c63a;
    --gold-deep: #b8961f;
    --ink: #3a3a3a;
    --ink-soft: #5b5b5b;
    --paper: #ffffff;
    --paper-shade: #efefef;
    --canvas: #f3f3f1;
    --cap: #141414;
  }
  * { box-sizing: border-box; margin: 0; padding: 0; }
  html, body { width: 1200px; height: 1200px; overflow: hidden; }
  body { background: var(--canvas); position: relative; font-family: "Roboto Condensed", sans-serif; color: var(--ink); }

  /* Bottle label, flat */
  .bottle-label {
    position: absolute; left: 50px; top: 360px; width: 340px; height: 470px;
    background: linear-gradient(90deg, var(--paper-shade), var(--paper) 30%, var(--paper) 70%, var(--paper-shade));
    border-left: 3px solid var(--gold); border-right: 3px solid var(--gold);
    overflow: hidden;
  }
  .brand { display: flex; align-items: center; gap: 12px; }
  .brand-dot { border-radius: 50%; background: var(--gold); flex: none; }
  .brand-name { font-family: "Josefin Sans", sans-serif; font-weight: 400; color: var(--ink-soft); letter-spacing: 2px; text-transform: uppercase; }
  .bottle-label .brand { position: absolute; left: 22px; top: 60px; }
  .bottle-label .brand-dot { width: 50px; height: 50px; }
  .bottle-label .brand-name { font-size: 20px; }

  .function { font-family: "Roboto Condensed", sans-serif; font-weight: 400; color: var(--ink); line-height: 1.05; text-transform: uppercase; letter-spacing: -0.5px; }
  .rule { background: var(--gold); height: 5px; }
  .product-name { font-family: "Exo 2", sans-serif; font-style: italic; font-weight: 300; color: var(--ink-soft); letter-spacing: 4px; }
  .category { font-family: "Roboto Condensed", sans-serif; font-weight: 300; color: var(--ink-soft); }
  .volume { font-family: "Roboto Condensed", sans-serif; font-weight: 400; color: var(--gold); }

  .bottle-label .function { position: absolute; left: 14px; top: 210px; font-size: 36px; }
  .bottle-label .rule { position: absolute; left: 14px; top: 304px; width: 246px; height: 4px; }
  .bottle-label .product-name { position: absolute; left: 16px; top: 320px; font-size: 28px; }
  .bottle-label .category { position: absolute; left: 12px; top: 400px; font-size: 24px; }
  .bottle-label .volume { position: absolute; left: 14px; top: 428px; font-size: 30px; letter-spacing: 1px; }
  .bottle-label .decor { position: absolute; right: -20px; top: 250px; width: 130px; height: 180px; }

  .decor { border-radius: 60px 60px 0 60px; background: radial-gradient(circle at 55% 45%, rgba(201,168,44,0.35), rgba(201,168,44,0.12) 60%, rgba(201,168,44,0) 75%); }

  /* Box front panel, flat */
  .box-front {
    position: absolute; left: 430px; top: 250px; width: 450px; height: 700px;
    background: linear-gradient(180deg, var(--paper), #f6f6f6);
    overflow: hidden;
  }
  .box-front .brand { position: absolute; left: 34px; top: 60px; gap: 16px; }
  .box-front .brand-dot { width: 90px; height: 90px; }
  .brand-lockup { display: flex; flex-direction: column; }
  .box-front .brand-name { font-size: 34px; padding-bottom: 4px; border-bottom: 3px solid var(--gold); }
  .slogan { font-family: "Josefin Sans", sans-serif; color: var(--ink-soft); font-size: 19px; letter-spacing: 2px; margin-top: 8px; }

  .box-front .function { position: absolute; left: 40px; top: 300px; font-size: 50px; font-weight: 400; transform: scaleX(0.88); transform-origin: left; }
  .box-front .rule { position: absolute; left: 40px; top: 422px; width: 300px; height: 6px; }
  .box-front .product-name { position: absolute; left: 44px; top: 440px; font-size: 40px; }
  .box-front .category { position: absolute; left: 40px; top: 580px; font-size: 30px; }
  .box-front .volume { position: absolute; left: 40px; top: 620px; font-size: 40px; font-weight: 700; }
  .box-front .decor { position: absolute; right: -60px; top: 430px; width: 220px; height: 300px; }

  /* Box information panel, flat */
  .box-side {
    position: absolute; left: 880px; top: 250px; width: 280px; height: 700px;
    background: linear-gradient(180deg, var(--gold-bright), var(--gold));
    color: var(--paper); padding: 46px 22px 0 22px; overflow: hidden;
  }
  .info-block { font-size: 19px; line-height: 1.3; text-align: justify; margin-bottom: 14px; }
  .info-block strong { font-weight: 700; }
  .box-side .decor { position: absolute; left: -40px; top: 420px; width: 300px; height: 280px;
    background: radial-gradient(circle at 40% 50%, rgba(255,255,255,0.45), rgba(255,255,255,0.15) 60%, rgba(255,255,255,0) 75%); }
</style>
</head>
<body>

<section class="bottle-label" aria-label="Bottle label">
  <div class="brand">
    <span class="brand-dot"></span>
    <span class="brand-name">Copper Lantern</span>
  </div>
  <h2 class="function">Testosterone<br>Support</h2>
  <div class="rule"></div>
  <p class="product-name">Tongkat Ali</p>
  <div class="decor" role="img" aria-label="Gold line-art brand flourish"></div>
  <p class="category">Dietary Supplement</p>
  <p class="volume">30ml / 1 fl oz</p>
</section>

<section class="box-front" aria-label="Box principal display panel">
  <div class="brand">
    <span class="brand-dot"></span>
    <div class="brand-lockup">
      <span class="brand-name">Copper Lantern</span>
      <span class="slogan">Quality Without Compromise</span>
    </div>
  </div>
  <h1 class="function">Testosterone<br>Support</h1>
  <div class="rule"></div>
  <p class="product-name">Tongkat Ali</p>
  <div class="decor" role="img" aria-label="Large gold line-art brand flourish"></div>
  <p class="category">Dietary Supplement</p>
  <p class="volume">30ml / 1 fl oz</p>
</section>

<section class="box-side" aria-label="Box information panel">
  <p class="info-block"><strong>Directions:</strong> As a dietary supplement, mix 30 grams (approx. two scoops) in eight ounces of water or any other beverage per day, or as directed by your health care practitioner.</p>
  <p class="info-block"><strong>Safety Warning:</strong> This is a natural product that may exhibit color, taste, and density variations from lot to lot. It contains naturally occuring nutrients; therefore amounts may vary within the pea protein and flavor profiles.</p>
  <div class="decor" role="img" aria-label="Large white line-art brand flourish continuing from the front"></div>
</section>

</body>
</html>
```